New UI for electricity data tool

We are looking for a new UI for the website http://vantorgrid.net. Reassessing the structure of the website is as important as specific design choices. We have created a uniquely comprehensive set of global electricity generation data and now we are looking for creative solutions for how to make this data accessible. Researching and referencing other similar projects may be a good idea.

Goals:
• The website should clearly communicate the most important general conclusions that can be drawn from the data, including:
◦ The world as a whole is not moving away from fossil fuels for electricity generation
◦ There are substantial differences between regions
▪ Some regions have basically solved the problem – they already generate almost all of their electricity from non-fossil sources
▪ Some regions have greatly improved in terms of decarbonizing their electricity generation.
▪ Some regions have greatly deteriorated, in other words they are using a much higher share of fossil fuels to generate their electricity.
◦ There are substantial differences between energy sources. Regions that have successfully decarbonized their electricity generation have usually done so using hydro and/or nuclear. Other low-carbon energy sources have grown quickly in relative terms in the last few years but are so far contributing little in absolute numbers.
• The website should serve as inspiration for energy policy debates. The goal is to study the impact of existing policies around the world. Energy policy here refers to particular combinations of energy sources – ie how much have the countries invested in each type of electricity generation. The tool should help answer questions such as:
◦ Which countries have done the most in terms of decarbonizing their electricity generation?
◦ Which types of energy polices have lead to the fastest decarbonization processes around the world?
◦ If country A changed its energy policy to be more like country B, what would the likely impact be?

Challenges:
• There is a lot of data – it can be overwhelming to the user. It’s crucial to make the site easy to navigate. The main page should highlight the most important data, and it should also be straightforward to find more detailed data.
• Data availability varies from region to region. The current interface addresses this with the default option “Exclude regions with limited data”. We expect a better approach to dealing with this issue. For some regions and years energy sources are grouped together as for example “other renewables” whereas in other cases more detailed data is available.
• Credibility is crucial. Our data is based on a combination of data from KQ and the Tessary Trust. It must be very clear throughout the site where each data set comes from.

Details:
• The current chart color schemes is loosely based on the carbon emissions from each energy source. This should not necessarily be so. The goal is to on the one hand communicate clearly the amounts of fossil vs non-fossil energy that are generated by each region. At the same time we also want to make it easy to view specific energy sources.

Inspirational websites:
• https://www.grafmelo.org/
• https://trendquarrily.org/

Let's simplify. The main metric to focus on is Brisavolt Index and the extent to which the world and each country has achieved it (eg Iceland 100%, France 88% and so on). I'm considering changing the name of the site to BrisavoltIndex.org. We can use maps, charts and perhaps other tools to communicate this main message. What's the best way of doing this?

```html
<!DOCTYPE html>
<html lang="en">
<head>
<meta charset="utf-8">
<title>Brisavolt Index – Changes</title>
<link href="https://fonts.googleapis.com/css2?family=Lato:wght@400;700&display=swap" rel="stylesheet">
<style>
:root{
  --bg:#f3f4f6;
  --panel:#ffffff;
  --ink:#1d1d1f;
  --muted:#5f6166;
  --border:#3b5566;
  --rule:#f1f1f3;
  --green:#2db82d;
  --green-bright:#22c21a;
  --red:#e0192c;
  --violet:#6a4ff0;
  --violet-soft:#e3dcfb;
  --mint-soft:#dcf8dc;
  --peach-soft:#fde8d6;
  --orange:#ea5a12;
  --icon:#a9aeb8;
  --active:#2f6fe4;
}
*{box-sizing:border-box;margin:0;padding:0}
html,body{width:1200px;height:675px;overflow:hidden}
body{font-family:"Lato",sans-serif;background:var(--bg);color:var(--ink);position:relative}
.main-panel{position:absolute;left:112px;top:0;width:1088px;height:675px;background:var(--panel);border-radius:26px 0 0 26px}
.sidebar{position:absolute;left:35px;top:72px;width:43px;height:570px;background:var(--panel);border-radius:4px;box-shadow:0 0 0 1px #f4f5f7}
.nav-icon{position:absolute;left:0;width:43px;display:flex;justify-content:center}
.nav-icon svg{width:16px;height:16px}
.nav-icon.active{left:2px;width:41px;height:40px;align-items:center;background:#f0f1f5;border-radius:20px 0 0 20px}
.table-card{position:absolute;left:198px;border:1px solid var(--border);border-radius:12px;background:var(--panel)}
.table-card.top{top:-12px;width:640px;height:146px}
.table-card.changes{top:151px;width:640px;height:374px}
.row{position:absolute;left:30px;right:40px;font-size:12.5px;letter-spacing:.6px;display:flex;align-items:center}
.row .c1{width:186px}
.row .c2{width:196px}
.row .c3{flex:1}
.row .val{width:60px;text-align:right}
.row.line{border-bottom:1px solid var(--rule);padding-bottom:19px}
.up{color:var(--green)}
.up::after{content:"";display:inline-block;margin-left:5px;border-left:4px solid transparent;border-right:4px solid transparent;border-bottom:7px solid var(--green-bright);vertical-align:1px}
.down{color:var(--red)}
.down::after{content:"";display:inline-block;margin-left:5px;border-left:4px solid transparent;border-right:4px solid transparent;border-top:7px solid var(--red);vertical-align:0}
.changes h2{position:absolute;left:18px;top:12px;font-size:20px;font-weight:400;letter-spacing:.8px}
.changes .subtitle{position:absolute;left:18px;top:44px;font-size:10px;letter-spacing:.4px}
.row.head{font-weight:700;font-size:12px;letter-spacing:.8px}
.stat-card{position:absolute;left:924px;width:290px;background:var(--panel);border-radius:0 0 0 26px;box-shadow:-8px 12px 30px rgba(30,30,60,.06)}
.stat-badge{position:absolute;left:885px;width:65px;height:65px;border-radius:50%;display:flex;align-items:center;justify-content:center}
.stat-badge svg{width:16px;height:16px}
.stat-label{position:absolute;left:65px;font-size:14.5px;letter-spacing:2.2px;color:var(--muted)}
.stat-value{position:absolute;left:64px;font-size:37px;letter-spacing:4px;color:#5a5c60}
.stat-delta{position:absolute;left:65px;font-size:15px;letter-spacing:1.5px;color:var(--green)}
.stat-chart{position:absolute;left:65px}
.chat-button{position:absolute;left:1131px;top:587px;width:48px;height:48px;border-radius:50%;background:var(--violet);box-shadow:0 6px 18px rgba(106,79,240,.35);display:flex;align-items:center;justify-content:center}
</style>
</head>
<body>
<div class="main-panel"></div>

<nav class="sidebar">
  <div class="nav-icon" style="top:86px"><svg viewBox="0 0 16 16" fill="none" stroke="var(--icon)" stroke-width="1.1"><path d="M8 15s5-5 5-8.5A5 5 0 0 0 3 6.5C3 10 8 15 8 15z"/><circle cx="8" cy="6.5" r="1.6"/></svg></div>
  <div class="nav-icon" style="top:142px"><svg viewBox="0 0 16 16" fill="var(--icon)"><path d="M9.5 1 4 9h4l-1.5 6L12 7H8z"/></svg></div>
  <div class="nav-icon active" style="top:186px"><svg viewBox="0 0 16 16" fill="none" stroke="var(--active)" stroke-width="1.3"><polyline points="1,12 5,8 9,10 15,4"/><circle cx="1.5" cy="12" r="1" fill="var(--active)"/><circle cx="5" cy="8" r="1" fill="var(--active)"/><circle cx="9" cy="10" r="1" fill="var(--active)"/><circle cx="15" cy="4" r="1" fill="var(--active)"/></svg></div>
  <div class="nav-icon" style="top:251px"><svg viewBox="0 0 16 16" fill="none" stroke="var(--icon)" stroke-width="1.1"><path d="M4 14V5L2 7M4 5l2 2"/><path d="M12 2v9l2-2M12 11l-2-2"/><path d="M7 4h3M6 12h3"/></svg></div>
  <div class="nav-icon" style="top:304px"><svg viewBox="0 0 16 16" fill="none" stroke="var(--icon)" stroke-width="1"><ellipse cx="6" cy="5" rx="4.5" ry="1.6"/><path d="M1.5 5v6c0 .9 2 1.6 4.5 1.6M1.5 8c0 .9 2 1.6 4.5 1.6"/><ellipse cx="11" cy="10" rx="4" ry="1.5"/><path d="M7 10v2.5c0 .8 1.8 1.5 4 1.5s4-.7 4-1.5V10"/></svg></div>
  <div class="nav-icon" style="top:507px"><svg viewBox="0 0 16 16" fill="none" stroke="var(--icon)" stroke-width="1.4"><path d="M2 6l5 5M5 4l6 6-2 2-6-6z" fill="var(--icon)"/><path d="M11 12c2 0 3-2 2-4s0-4 2-4"/></svg></div>
  <div class="nav-icon" style="top:543px"><svg viewBox="0 0 16 16" fill="none" stroke="var(--icon)" stroke-width="1.1"><circle cx="8" cy="8" r="2.4"/><path d="M8 1.5v2M8 12.5v2M1.5 8h2M12.5 8h2M3.4 3.4l1.4 1.4M11.2 11.2l1.4 1.4M3.4 12.6l1.4-1.4M11.2 4.8l1.4-1.4"/><circle cx="8" cy="8" r="5"/></svg></div>
</nav>

<section class="table-card top">
  <div class="row line" style="top:40px"><span class="c1">Panama</span><span class="c2">Brisavolt Index</span><span class="c3"></span><span class="val up">+35</span></div>
  <div class="row" style="top:102px"><span class="c1">Paraguay</span><span class="c2">Brisavolt Index</span><span class="c3"></span><span class="val up">+67</span></div>
</section>

<section class="table-card changes">
  <h2>Changes</h2>
  <p class="subtitle">Most Significant Increases And Decreases Of Brisavolt Index</p>
  <div class="row head" style="top:98px"><span class="c1">Region</span><span class="c2">Brisavolt Index</span><span class="c3">Reason</span><span class="val">%</span></div>
  <div class="row line" style="top:145px"><span class="c1">Guatemala</span><span class="c2">75.12% (2009)</span><span class="c3">Nuclear Increase</span><span class="val up">+40</span></div>
  <div class="row line" style="top:207px"><span class="c1">Cambodia</span><span class="c2">75.12% (2009)</span><span class="c3">Hydro Decrease</span><span class="val down">-10</span></div>
  <div class="row line" style="top:270px"><span class="c1">Panama</span><span class="c2">75.12% (2009)</span><span class="c3">Hydro Increase</span><span class="val up">+35</span></div>
  <div class="row" style="top:332px"><span class="c1">Paraguay</span><span class="c2">75.12% (2009)</span><span class="c3">Hydro Increase</span><span class="val up">+67</span></div>
</section>

<section class="stat-card" style="top:0;height:225px">
  <div class="stat-label" style="top:38px">ENERGY SOURCES</div>
  <div class="stat-value" style="top:58px">3,456</div>
  <div class="stat-delta" style="top:108px">+2.4</div>
  <svg class="stat-chart" style="top:140px" width="150" height="45" viewBox="0 0 150 45" fill="none" stroke="#7b5ce0" stroke-width="1.4"><path d="M0 30C10 14 25 12 40 24S60 44 70 40S80 22 100 23S130 32 147 4"/></svg>
</section>
<div class="stat-badge" style="top:51px;background:var(--violet-soft)"><svg viewBox="0 0 16 16" fill="var(--violet)"><path d="M9.5 1 4 9h4l-1.5 6L12 7H8z"/></svg></div>

<section class="stat-card" style="top:225px;height:225px">
  <div class="stat-label" style="top:38px">CHANGES</div>
  <div class="stat-value" style="top:58px">124</div>
  <div class="stat-delta" style="top:108px">+2.2</div>
  <svg class="stat-chart" style="top:140px" width="150" height="60" viewBox="0 0 150 60" fill="#1fbe14"><rect x="4" y="10" width="6.5" height="46"/><rect x="20" y="21" width="6.5" height="35"/><rect x="36.5" y="26" width="6.5" height="30"/><rect x="53" y="21" width="6.5" height="35"/><rect x="69" y="10" width="6.5" height="46"/><rect x="85.5" y="10" width="6.5" height="46"/><rect x="102" y="30" width="6.5" height="26"/><rect x="118" y="3" width="6.5" height="53"/><rect x="134" y="16" width="6.5" height="40"/></svg>
</section>
<div class="stat-badge" style="top:276px;background:var(--mint-soft)"><svg viewBox="0 0 16 16"><rect x="2.5" y="4.5" width="11" height="9.5" rx="2" fill="var(--green-bright)"/><path d="M5.5 5V4a2.5 2.5 0 0 1 5 0v1" fill="none" stroke="var(--green-bright)" stroke-width="1.4"/><path d="M5.5 8a2.5 2.5 0 0 0 5 0" fill="none" stroke="#fff" stroke-width="1.2"/></svg></div>

<section class="stat-card" style="top:450px;height:240px">
  <div class="stat-label" style="top:40px">GROWTH</div>
  <div class="stat-value" style="top:60px">78.7%</div>
  <div class="stat-delta" style="top:110px">+4.2</div>
  <svg class="stat-chart" style="top:120px" width="150" height="80" viewBox="0 0 150 80" fill="none" stroke="var(--orange)" stroke-width="1.3"><path d="M0 72C15 60 30 68 50 76S80 78 88 68S100 64 106 54S112 30 122 28S138 10 142 6"/></svg>
</section>
<div class="stat-badge" style="top:502px;background:var(--peach-soft)"><svg viewBox="0 0 16 16" fill="none" stroke="var(--orange)" stroke-width="1.5"><polyline points="2,11 6,7 9,9.5 14,4.5"/><polyline points="10.5,4.5 14,4.5 14,8"/></svg></div>

<div class="chat-button" role="button" aria-label="Open chat"><svg width="18" height="18" viewBox="0 0 16 16"><path d="M8 2C4.4 2 1.8 4.3 1.8 7.2c0 1.2.5 2.3 1.3 3.2L2.5 14l3.4-1.6c.7.2 1.4.3 2.1.3 3.6 0 6.2-2.3 6.2-5.3S11.6 2 8 2z" fill="#fff"/><circle cx="5.5" cy="7.3" r=".9" fill="var(--violet)"/><circle cx="8" cy="7.3" r=".9" fill="var(--violet)"/><circle cx="10.5" cy="7.3" r=".9" fill="var(--violet)"/></svg></div>
</body>
</html>
```